Paperback Book Cover Design

I need a professional cover designed for my new book. You must use the design template enclosed. The title of the book is “Open Your Digital Purse Now!” The graphic used on the book cover should of course relate to making money online through various skills such as writing, graphic design, online marketing, photography, trading, Tradlo etc. The graphic(s) used must demonstrate to the reader that the book gives various ways to make money online.

At the top of the book you must include the sub heading “Earn From Home Collection”. The main title of the book is “Open Your Digital Purse Now!”, which of course should be highly prominent on the front cover. The front cover must also include the author name, Gerald Whitcombe.

I have no preference to colours used so do be creative to create an eye catching cover design.

The spine of the book should include the main title and the author name. Feel free to use an image or images for the rear of the book and just add dummy text.

The winning designer must supply a layered psd file complete with all fonts and elements used.

Industry/Entity Type

Graphic Design

Requirements
Must have
• The winning designer must supply a layered psd file complete with all fonts and elements used.

```html
<!DOCTYPE html>
<html lang="en">
<head>
<meta charset="utf-8">
<title>Open Your Digital Purse Now! – Paperback Cover</title>
<link rel="stylesheet" href="https://fonts.googleapis.com/css2?family=Anton&family=Cinzel:wght@700&family=Didact+Gothic&family=Inter:wght@400&family=Permanent+Marker&display=swap">
<style>
  :root {
    --page: #ffffff;
    --green-bright: #3be11c;
    --green-deep: #17930a;
    --green-dark: #0f2a04;
    --scene-light: #f4f7a8;
    --scene-mid: #9ccc2c;
    --scene-dark: #16330a;
    --gold: #ffd21a;
    --white: #ffffff;
    --ink: #1a2605;
    --body-ink: rgba(20, 35, 5, 0.85);
  }
  * { margin: 0; padding: 0; box-sizing: border-box; }
  html, body { width: 1200px; height: 1000px; overflow: hidden; background: var(--page); }
  .canvas { position: relative; width: 1200px; height: 1000px; }

  .cover-spread {
    position: absolute; left: 18px; top: 80px; width: 1167px; height: 810px;
    overflow: hidden; box-shadow: 4px 5px 8px rgba(0,0,0,0.45);
  }
  .scene-art {
    position: absolute; inset: 0;
    background:
      radial-gradient(ellipse 420px 260px at 700px 250px, var(--scene-light) 0%, rgba(220,235,110,0.7) 35%, rgba(156,204,44,0) 75%),
      linear-gradient(180deg, #2d5a10 0%, #5f9a1c 22%, #8cc22c 38%, #7db528 55%, #3f7414 78%, var(--scene-dark) 100%);
  }
  .rear-text-band {
    position: absolute; left: 266px; top: 0; width: 196px; height: 520px;
    background: linear-gradient(180deg, rgba(255,255,255,0.16), rgba(255,255,255,0.05));
  }

  /* Shared type */
  .series-line { position: absolute; font-family: "Didact Gothic", sans-serif; color: var(--white); white-space: nowrap; }
  .title-word {
    display: block; font-family: "Anton", sans-serif; color: var(--green-bright);
    text-transform: uppercase; text-align: center; white-space: nowrap;
    text-shadow: 1px 1px 0 var(--green-deep), 2px 2px 0 var(--green-dark), 3px 4px 6px rgba(0,0,0,0.45);
  }
  .title-flourish {
    position: absolute; font-family: "Permanent Marker", cursive; color: var(--gold);
    white-space: nowrap; text-shadow: 2px 2px 0 rgba(60,40,0,0.6);
  }
  .bracket { position: absolute; border: 0 solid var(--white); }
  .bracket-left { border-left-width: var(--bw); border-top-width: var(--bw); border-bottom-width: var(--bw); }
  .bracket-right { border-right-width: var(--bw); border-top-width: var(--bw); border-bottom-width: var(--bw); }

  /* Rear cover */
  .rear-series { left: 22px; top: 22px; font-size: 19px; }
  .rear-bracket { --bw: 14px; left: 4px; top: 46px; width: 40px; height: 222px; }
  .rear-title { position: absolute; left: 40px; top: 58px; width: 190px; }
  .rear-title .title-word { font-size: 46px; line-height: 43px; }
  .rear-flourish { left: 90px; top: 228px; font-size: 44px; transform: rotate(-14deg); }

  .rear-copy {
    position: absolute; left: 272px; top: 20px; width: 186px;
    font-family: "Inter", sans-serif; font-size: 6.6px; line-height: 8.6px;
    color: var(--body-ink); text-align: justify;
  }
  .rear-copy p + p { margin-top: 9px; }

  /* Spine */
  .spine-series {
    position: absolute; left: 595px; top: 16px; writing-mode: vertical-rl;
    font-family: "Didact Gothic", sans-serif; font-size: 25px; color: var(--ink); white-space: nowrap;
  }
  .spine-title {
    position: absolute; left: 545px; top: 14px; writing-mode: vertical-rl;
    font-family: "Anton", sans-serif; font-size: 44px; line-height: 50px; color: var(--green-bright);
    text-shadow: 1px 1px 0 var(--green-dark); white-space: nowrap; letter-spacing: 0.5px;
  }
  .spine-author {
    position: absolute; left: 548px; top: 728px; width: 80px; text-align: center;
    font-family: "Cinzel", serif; font-weight: 700; font-size: 13px; line-height: 15px; color: var(--ink);
  }

  /* Front cover */
  .front-series { left: 648px; top: 28px; font-size: 42px; letter-spacing: 0.5px; text-shadow: 1px 1px 3px rgba(0,0,0,0.4); }
  .front-bracket-left { --bw: 20px; left: 642px; top: 76px; width: 46px; height: 536px; }
  .front-bracket-right { --bw: 20px; left: 1108px; top: 76px; width: 46px; height: 536px; }
  .front-title { position: absolute; left: 672px; top: 76px; width: 454px; }
  .front-title .title-word { font-size: 150px; line-height: 126px; }
  .front-title .word-wide { transform: scaleX(0.82); }
  .front-flourish { left: 790px; top: 555px; font-size: 92px; transform: rotate(-12deg); }
  .front-author {
    position: absolute; left: 700px; top: 758px; width: 440px; text-align: center;
    font-family: "Cinzel", serif; font-weight: 700; font-size: 30px; color: var(--ink); white-space: nowrap;
  }
</style>
</head>
<body>
<main class="canvas">
  <section class="cover-spread">
    <div class="scene-art" role="img" aria-label="Green-lit digital scene of desktop computers and keyboards arranged in a circle on a floor of binary digits, linked by glowing network lines"></div>
    <div class="rear-text-band"></div>

    <!-- Rear cover -->
    <p class="series-line rear-series">Earn From Home Collection:</p>
    <div class="bracket bracket-left rear-bracket"></div>
    <h2 class="rear-title">
      <span class="title-word">Open</span>
      <span class="title-word">Your</span>
      <span class="title-word">Digital</span>
      <span class="title-word">Purse</span>
    </h2>
    <p class="title-flourish rear-flourish">Now!</p>

    <div class="rear-copy">
      <p>Earning a steady income from home is no longer a distant dream. This collection walks you through proven paths that ordinary people use every day to turn their skills, spare hours and curiosity into reliable online revenue.</p>
      <p>Inside you will find clear steps for freelance writing, graphic design, photography, online marketing and trading, each explained in plain language with practical checklists you can follow from your very first afternoon.</p>
      <p>Learn how to choose the right platform, price your work with confidence, build a small portfolio, and win repeat clients without spending money on expensive courses or tools you do not need.</p>
      <p>Discover how sellers on Tradlo source simple products, write listings that attract buyers, and manage shipping so that every sale adds up to real profit at the end of each month.</p>
      <p>Whether you want a little extra cash or a full new career, these pages show you where to begin, what to avoid, and how to keep growing once the first payments arrive.</p>
      <p>Open your digital purse today and start building the flexible, rewarding working life you have always wanted.</p>
    </div>

    <!-- Spine -->
    <p class="spine-series">Earn From Home Collection:</p>
    <p class="spine-title">OPEN YOUR DIGITAL PURSE NOW!</p>
    <p class="spine-author">By:<br>Gerald<br>Whitcombe</p>

    <!-- Front cover -->
    <p class="series-line front-series">Earn From Home Collection:</p>
    <div class="bracket bracket-left front-bracket-left"></div>
    <div class="bracket bracket-right front-bracket-right"></div>
    <h1 class="front-title">
      <span class="title-word">Open</span>
      <span class="title-word">Your</span>
      <span class="title-word word-wide">Digital</span>
      <span class="title-word">Purse</span>
    </h1>
    <p class="title-flourish front-flourish">Now!</p>
    <p class="front-author">By: Gerald Whitcombe</p>
  </section>
</main>
</body>
</html>
```